Halvern Equity Lettehead project

we need letterhead for a new company in NJ called Halvern Equity, llc. We finance sub-prime auto loans from all over the US. We'd like to see letterhead that incorporates the logo we recently had designed on
PixelHarbor. The final design should have a rich and traditional look to it

Target Market(s)

Traditional Investment Banks in the US & Europe

Industry/Entity Type

Finance

Font styles to use
Other font styles liked:
• Centaur, Times New Roman, Serif

Requirements
Must have
• Our logo and the address & contact info for both our locations:
• 9 Mossley Ct, Suite 248, Red Bank, NJ 07702 - Dealer Relations - Portfolio Development
• 417 Quarry Lane, Bernards Township, NJ 07920 - Investor Relations - Portfolio Mgmt
• T: 732.555.0172 F: 732.555.0846

```html
<!DOCTYPE html>
<html lang="en">
<head>
<meta charset="utf-8">
<title>Halvern Equity Letterhead</title>
<link rel="stylesheet" href="https://fonts.googleapis.com/css2?family=Tinos&family=Source+Sans+3:wght@400&display=swap">
<style>
  :root {
    --backdrop: #e6e6e6;
    --paper: #efeff0;
    --ink: #1d1d1d;
    --mark: #231f20;
    --name-grey: #9c9c9c;
    --signature-blue: #9aa6c4;
  }
  * { margin: 0; padding: 0; box-sizing: border-box; }
  html, body { width: 1113px; height: 1200px; overflow: hidden; background: var(--backdrop); }
  .sheet {
    position: absolute; left: 91px; top: 58px; width: 768px; height: 1085px;
    background: var(--paper); color: var(--ink);
  }
  .brand { position: absolute; left: 43px; top: 41px; display: flex; align-items: center; }
  .brand-circle { width: 108px; height: 108px; border-radius: 50%; background: var(--mark); }
  .brand-name {
    margin-left: 14px; font-family: "Tinos", serif; font-size: 23px; font-weight: 400;
    letter-spacing: 0.5px; color: var(--name-grey); white-space: nowrap;
  }
  .contact-lines {
    position: absolute; left: 627px; top: 77px;
    font-family: "Tinos", serif; font-size: 14px; line-height: 19px;
  }
  .salutation {
    position: absolute; left: 112px; top: 297px; font-weight: 400;
    font-family: "Source Sans 3", sans-serif; font-size: 22px;
  }
  .letter-body {
    position: absolute; left: 112px; top: 364px; width: 543px;
    font-family: "Source Sans 3", sans-serif; font-size: 13px; line-height: 19.7px;
    letter-spacing: 0.2px; text-align: justify;
  }
  .letter-body p + p { margin-top: 19.7px; }
  .signature-mark {
    position: absolute; left: 485px; top: 728px; width: 155px; height: 62px;
    background: linear-gradient(90deg, rgba(154,166,196,0.25), rgba(154,166,196,0.12));
    border-radius: 30px;
  }
  .closing {
    position: absolute; left: 579px; top: 742px;
    font-family: "Source Sans 3", sans-serif; font-size: 12px;
  }
  .office {
    position: absolute; top: 1003px; font-style: normal;
    font-family: "Tinos", serif; font-size: 14.5px; line-height: 19px;
  }
  .office-north { left: 24px; letter-spacing: 0.45px; }
  .office-south { right: 23px; text-align: right; font-size: 14px; }
</style>
</head>
<body>
  <main class="sheet">
    <header>
      <div class="brand">
        <div class="brand-circle"></div>
        <span class="brand-name">Halvern Equity, llc</span>
      </div>
      <div class="contact-lines">
        <div>T: 732.555.0172</div>
        <div>F: 732.555.0846</div>
      </div>
    </header>

    <h1 class="salutation">Dear Mr. Carver,</h1>

    <section class="letter-body">
      <p>Lorem ipsum dolor sit amet, consectetur adipiscing elit. Donec orci purus, luctus vitae dignissim eu, iaculis sed purus. Vivamus faucibus, ipsum nec aliquet viverra, leo mauris condimentum ligula, sit amet sagittis enim ligula quis arcu. Nam egestas tortor id nisi porttitor mattis. In tortor ante, ultricies in suscipit a, tempus non massa. Vivamus et auctor mi. Fusce vel massa nulla. Phasellus nec eros mauris, et scelerisque orci.</p>
      <p>Donec malesuada orci vitae nulla accumsan porta a id massa. Quisque accumsan iaculis magna sit amet fringilla. Maecenas consequat, magna eget tincidunt semper, odio nibh rutrum mi, id feugiat ante nisi eu risus. Vestibulum nunc orci, rhoncus a placerat in, ultricies in mi. Cras mattis varius eros, vel fringilla nisi suscipit eget. Quisque scelerisque sagittis nulla at porttitor.</p>
      <p>Sed id augue vitae urna euismod commodo aliquet a quam. Pellentesque arcu velit, cursus et malesuada ut, consequat et diam. Nullam erat sem, rhoncus id ullamcorper vitae, rhoncus et arcu. In ultricies ultricies nulla, ut rutrum nisi iaculis at. Donec eu magna a metus ornare faucibus. Fusce aliquet faucibus ultricies. Morbi semper, est id tincidunt gravida, sem arcu adipiscing lacus, ac bibendum nulla leo eu purus. Quisque nec diam sed risus consectetur a ccumsan quis quis nibh. Vestibulum id purus lorem.</p>
    </section>

    <div class="signature-mark" role="img" aria-label="Handwritten signature of the sender in blue ink"></div>
    <div class="closing">Sincerely,</div>

    <footer>
      <address class="office office-north">
        417 Quarry Lane,<br>
        Bernards Township,<br>
        NJ 07920 - Investor Relations - Portfolio Mgmt
      </address>
      <address class="office office-south">
        9 Mossley Ct, Suite 248<br>
        Red Bank, NJ 07702<br>
        Dealer Relations - Portfolio Development
      </address>
    </footer>
  </main>
</body>
</html>
```